Willowbend Spine Chiropractic

office phone- 913-462-1037
After Hour number 913-284-6150
Office address 27814 Halvorn Rd. Overland Park Ks 66947
Dr. Marlon Pettigrew, DC
I added 3 different types of logos proofs.
Specalizing in:
Family Wellness Care
Auto Accident
Workman Comp Injuries
Urgent Alternative Pain Relief
Non-operative Sports Injury Care

```html
<!DOCTYPE html>
<html lang="en">
<head>
<meta charset="utf-8">
<title>Willowbend Spine Chiropractic – Business Card</title>
<link rel="stylesheet" href="https://fonts.googleapis.com/css2?family=Saira+Condensed:wght@700&family=Tinos:wght@400;700&family=Electrolize&family=Roboto:wght@400;700&display=swap">
<style>
  :root {
    --navy: #27286a;
    --navy-deep: #1f2060;
    --paper: #f4f4f6;
    --ink-black: #141414;
    --olive: #6f7a3c;
    --grey-text: #4a4a4a;
    --accent-red: #c0283a;
    --backdrop: #d9d9dc;
  }
  * { margin: 0; padding: 0; box-sizing: border-box; }
  html, body { width: 1200px; height: 960px; overflow: hidden; }
  body { background: var(--backdrop); position: relative; }

  .card {
    position: absolute;
    left: 250px;
    width: 700px;
    height: 420px;
    box-shadow: 0 6px 18px rgba(0,0,0,.18);
  }
  .card-back { top: 40px; background: var(--navy); }
  .card-front { top: 500px; background: var(--paper); overflow: hidden; }
  .card-shapes { position: absolute; inset: 0; }

  .brand {
    position: absolute;
    display: flex;
    align-items: center;
    gap: 10px;
    font-family: "Saira Condensed", sans-serif;
    font-weight: 700;
    color: #ffffff;
    text-transform: uppercase;
    letter-spacing: .5px;
    white-space: nowrap;
  }
  .brand-mark { width: 14px; height: 14px; background: #ffffff; flex: none; }
  .card-back .brand { left: 0; right: 0; top: 184px; justify-content: center; font-size: 40px; }
  .card-back .brand-mark { width: 18px; height: 18px; }
  .card-front .brand { left: 150px; width: 530px; top: 50px; justify-content: center; font-size: 32px; }

  .doctor-name {
    position: absolute; left: 70px; top: 158px;
    font-family: "Tinos", serif; font-size: 30px; color: #111;
    letter-spacing: 1px;
  }
  .doctor-name strong { font-weight: 700; }

  .specialties { position: absolute; left: 70px; top: 204px; }
  .specialties-title {
    display: flex; align-items: center; gap: 8px;
    font-family: "Roboto", sans-serif; font-weight: 700; font-size: 17px; color: var(--navy);
  }
  .specialties-title::before {
    content: ""; width: 10px; height: 10px; background: var(--accent-red);
  }
  .specialties-list {
    list-style: none; margin-top: 4px;
    font-family: "Electrolize", sans-serif; font-size: 12.5px; line-height: 15px;
    font-variant: small-caps; letter-spacing: 1.4px; color: var(--olive);
  }

  .contact-row {
    position: absolute; left: 70px; width: 600px;
    font-family: "Roboto", sans-serif; font-size: 14px; line-height: 17px;
    color: var(--grey-text); letter-spacing: .6px;
  }
  .contact-row.address { top: 312px; }
  .contact-row.office-phone { top: 354px; }
  .contact-row.after-hours { top: 386px; }
</style>
</head>
<body>

  <section class="card card-back" aria-label="Card back">
    <div class="brand"><span class="brand-mark"></span>Willowbend Spine Chiropractic</div>
  </section>

  <section class="card card-front" aria-label="Card front">
    <svg class="card-shapes" viewBox="0 0 700 420" width="700" height="420" aria-hidden="true">
      <!-- header panel -->
      <polygon points="150,22 680,22 680,100 640,140 190,140 150,100" fill="var(--navy)"/>
      <!-- left edge band -->
      <polygon points="0,40 26,70 26,370 0,400" fill="var(--ink-black)"/>
      <!-- contact rules -->
      <line x1="60" y1="306" x2="625" y2="306" stroke="var(--navy)" stroke-width="1.5"/>
      <line x1="60" y1="348" x2="625" y2="348" stroke="var(--navy)" stroke-width="1.5"/>
      <line x1="60" y1="380" x2="625" y2="380" stroke="var(--navy)" stroke-width="1.5"/>
      <!-- icon tiles -->
      <rect x="630" y="308" width="30" height="30" fill="var(--navy)"/>
      <rect x="630" y="350" width="28" height="28" fill="var(--navy)"/>
      <rect x="630" y="382" width="28" height="28" fill="var(--navy)"/>
      <!-- pin icon -->
      <path d="M645 314 a7 7 0 0 1 7 7 c0 5 -7 11 -7 11 s-7 -6 -7 -11 a7 7 0 0 1 7 -7z" fill="#fff"/>
      <circle cx="645" cy="321" r="2.6" fill="var(--navy)"/>
      <!-- desk phone icon -->
      <rect x="636" y="362" width="16" height="10" rx="2" fill="#fff"/>
      <path d="M635 360 q9 -6 18 0 v3 h-4 v-2 h-10 v2 h-4z" fill="#fff"/>
      <circle cx="644" cy="367" r="2.5" fill="var(--navy)"/>
      <!-- handset icon -->
      <path d="M639 388 q-2 2 0 6 q4 8 11 11 q4 2 6 -1 l-3 -3 q-2 1 -3 0 q-4 -2 -6 -6 q-1 -1 0 -3z" fill="#fff"/>
    </svg>

    <div class="brand"><span class="brand-mark"></span>Willowbend Spine Chiropractic</div>

    <p class="doctor-name"><strong>Dr. Marlon</strong> Pettigrew</p>

    <div class="specialties">
      <p class="specialties-title">Specializing in:</p>
      <ul class="specialties-list">
        <li>Family Wellness Care</li>
        <li>Auto Accident</li>
        <li>Workman Comp Injuries</li>
        <li>Urgent Alternative Pain Relief</li>
        <li>Non-operative Sports Injury Care</li>
      </ul>
    </div>

    <p class="contact-row address">27814 Halvorn Rd.<br>Overland Park Ks 66947</p>
    <p class="contact-row office-phone">913-462-1037</p>
    <p class="contact-row after-hours">913-284-6150</p>
  </section>

</body>
</html>
```